Marlow Naturopathics business card design

Using the marlow logo designed, we would like that incorporated into a business card. A colour scheme which works with the logo and lists the following business details:

Dennis Marlow - Naturopath
Level 1, 58 Torvane Street
Wollongong NSW
(02) 4391 7084
www.dennismarlowhealth-example.com

We would also like space on the back of the card for next appointment times.

Target Market(s)

Anyone looking to improve their health

Industry/Entity Type

Business

Requirements
Must have
• Marlow Naturopathics logo, business details.
Nice to have
• Good colour schemes, attractive, eye-catching features that are easy to read.

```html
<!DOCTYPE html>
<html lang="en">
<head>
<meta charset="utf-8">
<title>Marlow Naturopathics – Business Card</title>
<link rel="stylesheet" href="https://fonts.googleapis.com/css2?family=Ropa+Sans&display=swap">
<style>
  :root {
    --page: #ffffff;
    --card: #55504a;
    --card-grain: #5b5650;
    --mark: #262320;
    --ink: #f1ebe1;
    --ink-soft: #ddd5c8;
    --rule: #bfb6a8;
  }
  * { margin: 0; padding: 0; box-sizing: border-box; }
  html, body {
    width: 1200px;
    height: 900px;
    overflow: hidden;
    background: var(--page);
  }
  body {
    position: relative;
    font-family: "Ropa Sans", sans-serif;
    color: var(--ink);
  }
  .card {
    position: absolute;
    left: 265px;
    width: 663px;
    height: 410px;
    background: radial-gradient(circle at 50% 45%, var(--card-grain), var(--card));
  }
  .card--front { top: 23px; }
  .card--back { top: 457px; }

  .brand {
    position: absolute;
    display: flex;
    flex-direction: column;
    align-items: center;
    color: var(--ink);
  }
  .brand__mark {
    border-radius: 50%;
    background: var(--mark);
  }
  .brand__name {
    white-space: nowrap;
    line-height: 1;
  }

  .card--front .brand {
    left: 0; right: 0;
    top: 84px;
  }
  .card--front .brand__mark { width: 96px; height: 96px; margin-bottom: 20px; }
  .card--front .brand__name { font-size: 34px; }

  .appointment {
    position: absolute;
    left: 151px;
    top: 272px;
    width: 360px;
    color: var(--ink-soft);
  }
  .appointment__title {
    font-size: 17px;
    letter-spacing: 2px;
    text-transform: uppercase;
    text-align: center;
    margin-bottom: 14px;
  }
  .appointment__row {
    display: flex;
    gap: 22px;
    font-size: 17px;
    margin-bottom: 14px;
  }
  .appointment__field {
    flex: 1;
    display: flex;
    align-items: flex-end;
    gap: 8px;
  }
  .appointment__line {
    flex: 1;
    border-bottom: 1px solid var(--rule);
    height: 18px;
  }

  .card--back .brand {
    left: 30px;
    top: 36px;
    width: 130px;
  }
  .card--back .brand__mark { width: 52px; height: 52px; margin-bottom: 12px; }
  .card--back .brand__name { font-size: 16px; }

  .holder {
    position: absolute;
    left: 393px;
    top: 80px;
  }
  .holder__name {
    font-size: 40px;
    line-height: 1;
    color: var(--ink);
  }
  .holder__role {
    font-size: 28px;
    line-height: 1;
    margin: 10px 0 0 7px;
    color: var(--ink-soft);
  }

  .contact {
    position: absolute;
    left: 327px;
    top: 282px;
    list-style: none;
    font-size: 20px;
    line-height: 27px;
    color: var(--ink-soft);
    white-space: nowrap;
  }
</style>
</head>
<body>
  <section class="card card--front" aria-label="Card front">
    <div class="brand">
      <span class="brand__mark"></span>
      <span class="brand__name">Marlow Naturopathics</span>
    </div>

    <div class="appointment">
      <p class="appointment__title">Next appointment</p>
      <div class="appointment__row">
        <span class="appointment__field">Date <span class="appointment__line"></span></span>
        <span class="appointment__field">Time <span class="appointment__line"></span></span>
      </div>
      <div class="appointment__row">
        <span class="appointment__field">Date <span class="appointment__line"></span></span>
        <span class="appointment__field">Time <span class="appointment__line"></span></span>
      </div>
    </div>
  </section>

  <section class="card card--back" aria-label="Card back">
    <div class="brand">
      <span class="brand__mark"></span>
      <span class="brand__name">Marlow Naturopathics</span>
    </div>

    <div class="holder">
      <p class="holder__name">Dennis Marlow</p>
      <p class="holder__role">Naturopath</p>
    </div>

    <ul class="contact">
      <li>Level 1, 58 Torvane Street</li>
      <li>Wollongong NSW</li>
      <li>(02) 4391 7084</li>
      <li>www.dennismarlowhealth-example.com</li>
    </ul>
  </section>
</body>
</html>
```